Design logo, business cards, and web page for new web and bi development consulting company

I've started a Web and Business Intelligence development consulting company. We develop on Bramquist's stack, Vantage Sudio and Querion Server. We develop responsive web sites and business intelligence platforms. I plan on focusing on small to medium sized business as my client base. I need a logo, business cards, and a one page web site. We will do more with the web site with you in the next six months if the business survives. The name of the company is Korvale Integration Solutions, Korvale for short.

Target Market(s)

small to medium sized businesses

Industry/Entity Type

Business

Contact Information for Business Card

logo
name
title
email
phone

Logo Text

Korvale Integration Solutions - web and data solutions

Coding

Coded - Design and coding required

Number of Pages Required

1 page

Font styles to use
Sans Serif

Colors
0355a3
0092cd
00a88f
6b449b

Requirements
Nice to have
• web and data solutions

```html
<!DOCTYPE html>
<html lang="en">
<head>
<meta charset="utf-8">
<title>Korvale Integration Solutions</title>
<link rel="stylesheet" href="https://fonts.googleapis.com/css2?family=Lato:wght@300;400;700&display=swap">
<style>
:root{
  --purple:#6b449b;
  --purple-dark:#5a3688;
  --navy:#0355a3;
  --blue:#0092cd;
  --teal:#00a88f;
  --text:#444;
  --heading:#333;
  --grey-band:#f4f4f4;
  --white:#fff;
}
*{margin:0;padding:0;box-sizing:border-box}
html,body{width:1200px;height:4018px;overflow:hidden}
body{position:relative;font-family:'Lato',sans-serif;color:var(--text);background:var(--white)}
/* Header */
.hero{position:absolute;left:0;top:0;width:1200px;height:501px;background:var(--purple)}
.brand{position:absolute;left:110px;top:30px;color:var(--white)}
.brand-name{font-weight:700;font-size:40px;line-height:40px;letter-spacing:-1px}
.brand-tag{font-size:12px;margin-top:2px}
.search{position:absolute;left:760px;top:29px;width:237px;height:22px;background:var(--purple-dark);color:#cbb9e0;font-size:10px;padding:4px 8px}
.search svg{position:absolute;right:6px;top:4px}
.social-dot{position:absolute;top:33px;width:14px;height:14px;border-radius:50%;background:rgba(255,255,255,.85)}
.nav{position:absolute;top:68px;right:93px;display:flex;font-size:20px;color:var(--white)}
.nav span{margin-left:44px}
.hero-title{position:absolute;left:110px;top:220px;width:350px;font-size:30px;line-height:40px;color:var(--white);font-weight:400}
.btn-more{position:absolute;left:110px;top:370px;width:163px;height:46px;background:var(--blue);color:var(--white);font-size:19px;line-height:46px;text-align:center}
.hero-art{position:absolute;left:480px;top:200px;width:592px;height:232px;background:linear-gradient(135deg,#8e6bb8,#a7d4e4 55%,#e6e2d6);border-radius:6px}
.dots{position:absolute;left:566px;top:462px;display:flex;gap:10px}
.dots i{display:block;width:8px;height:8px;border-radius:50%;background:var(--white)}
.dots i:first-child{background:none;border:1px solid var(--white)}
/* Services */
.section-title{position:absolute;left:0;width:1200px;text-align:center;font-weight:400}
.services-title{top:560px;font-size:42px;color:var(--heading)}
.service{position:absolute;top:660px;width:290px;text-align:center}
.service-mark{height:70px;display:flex;align-items:center;justify-content:center;gap:10px;font-size:28px;font-weight:700}
.service-mark .sq{width:22px;height:22px}
.service h3{margin-top:48px;font-size:27px;font-weight:400;color:var(--heading)}
.service p{margin-top:22px;font-size:15px;line-height:26px;padding:0 12px}
.btn-outline{display:inline-block;margin-top:44px;width:142px;height:38px;border:2px solid var(--purple);color:var(--heading);font-size:15px;line-height:34px}
.shadow-rule{position:absolute;left:160px;top:1118px;width:880px;height:14px;background:radial-gradient(ellipse at top,rgba(0,0,0,.12),transparent 70%)}
/* BI */
.bi-title{top:1208px;font-size:40px;color:var(--navy)}
.bi-lead{position:absolute;left:110px;top:1282px;width:980px;text-align:center;font-size:15px;line-height:26px}
.feature h3{position:absolute;font-size:32px;font-weight:400}
.feature p{position:absolute;width:550px;font-size:15px;line-height:26px}
.circle{position:absolute;border-radius:50%;display:flex;align-items:center;justify-content:center}
/* Responsive */
.band{position:absolute;left:0;top:2511px;width:1200px;height:1201px;background:var(--grey-band)}
.resp-title{top:2576px;font-size:40px;color:var(--navy)}
.devices{position:absolute;left:308px;top:2667px;width:603px;height:313px;background:linear-gradient(180deg,#d9dde2,#b9c3cc);border-radius:8px}
.resp-lead{position:absolute;left:110px;top:3020px;width:980px;text-align:center;font-size:15px;line-height:26px}
.recent-title{top:3148px;font-size:32px;color:var(--purple)}
.rule{position:absolute;left:110px;top:3215px;width:980px;height:1px;background:#ddd}
.layout-card{position:absolute;top:3245px;width:310px}
.thumb{width:310px;height:193px;background:linear-gradient(160deg,#2a2a2a,#6d6d6d);box-shadow:0 6px 8px rgba(0,0,0,.25)}
.layout-card h4{margin-top:54px;font-size:21px;font-weight:400;color:var(--purple)}
.layout-card p{margin-top:10px;width:280px;font-size:15px;line-height:26px}
.btn-details{display:block;margin-top:16px;width:107px;height:32px;background:var(--teal);color:var(--white);font-size:12px;line-height:32px;text-align:center}
/* Footer */
.foot-brand{position:absolute;left:110px;top:3757px;color:var(--purple)}
.foot-brand .brand-name{font-size:40px}
.foot-brand .brand-tag{font-size:12px;color:var(--purple)}
.foot-col{position:absolute;top:3757px;font-size:13px;color:#222}
.foot-col h5{font-size:15px;font-weight:400;color:var(--navy);margin-bottom:16px}
.foot-col li{list-style:none;line-height:26px}
.contact-row{display:flex;gap:10px;line-height:22px;margin-bottom:10px;font-size:12px;white-space:nowrap}
.contact-row i{flex:none;width:10px;height:10px;margin-top:6px;border-radius:50%;background:var(--teal)}
.follow{display:flex;justify-content:space-between;width:110px;margin-bottom:28px}
.follow i{width:10px;height:10px;border-radius:50%;background:var(--blue);margin-top:6px}
.copy-rule{position:absolute;left:0;top:3961px;width:1200px;height:1px;background:#e2e2e2}
.copy{position:absolute;left:0;top:3980px;width:1200px;text-align:center;font-size:12px;color:#222}
</style>
</head>
<body>

<header class="hero">
  <div class="brand"><div class="brand-name">Korvale</div><div class="brand-tag">Korvale Integration Solutions</div></div>
  <div class="search">Search
    <svg width="14" height="14" viewBox="0 0 14 14"><circle cx="6" cy="6" r="4" fill="none" stroke="#fff" stroke-width="2"/><line x1="9" y1="9" x2="13" y2="13" stroke="#fff" stroke-width="2"/></svg>
  </div>
  <span class="social-dot" style="left:1018px"></span>
  <span class="social-dot" style="left:1066px"></span>
  <nav class="nav"><span>Home</span><span>About Us</span><span>Our Services</span><span>Events</span><span>Careers</span><span>Contact Us</span></nav>
  <h1 class="hero-title">A Web and Business Intelligence Development Consulting Company</h1>
  <div class="btn-more">Learn More</div>
  <div class="hero-art" role="img" aria-label="Illustration of a laptop showing charts beside a phone, a clipboard and a bar graph"></div>
  <div class="dots"><i></i><i></i><i></i><i></i></div>
</header>

<h2 class="section-title services-title">Our Services</h2>
<div class="service" style="left:123px">
  <div class="service-mark" style="color:#1c6fb8"><span class="sq" style="background:#1c6fb8"></span>Nexa</div>
  <h3>Bramquist's stack</h3>
  <p>Lorem Ipsum is simply dummy text of the printing and typesetting industry. Lorem Ipsum has been the industry's standard dummy text ever since the 1500s, when an unknown printer took a galley</p>
  <span class="btn-outline">Read More</span>
</div>
<div class="service" style="left:455px">
  <div class="service-mark" style="color:var(--purple)"><span class="sq" style="background:var(--purple)"></span>Vantage Studio</div>
  <h3>Vantage Sudio</h3>
  <p>Lorem Ipsum is simply dummy text of the printing and typesetting industry. Lorem Ipsum has been the industry's standard dummy text ever since the 1500s, when an unknown printer took a galley</p>
  <span class="btn-outline">Read More</span>
</div>
<div class="service" style="left:787px">
  <div class="service-mark" style="color:#b32025"><span class="sq" style="background:#b32025"></span>Querion Server</div>
  <h3>Querion Server</h3>
  <p>Lorem Ipsum is simply dummy text of the printing and typesetting industry. Lorem Ipsum has been the industry's standard dummy text ever since the 1500s, when an unknown printer took a galley</p>
  <span class="btn-outline">Read More</span>
</div>
<div class="shadow-rule"></div>

<h2 class="section-title bi-title">Business Intelligence Platform</h2>
<p class="bi-lead">Lorem Ipsum is simply dummy text of the printing and typesetting industry. Lorem Ipsum has been the industry's standard dummy text ever since the 1500s, when an unknown printer took a galley of type and scrambled it to make a type specimen book.</p>

<section class="feature">
  <h3 style="left:110px;top:1458px;color:var(--blue)">Analysis</h3>
  <p style="left:110px;top:1524px">Lorem Ipsum is simply dummy text of the printing and typesetting industry. Lorem Ipsum has been the industry's standard dummy text ever since the 1500s, when an unknown printer took a galley of type and scrambled it to make a type specimen book. It has survived not only five centuries, but also the leap into electronic typesetting, remaining essentially unchanged.</p>
  <div class="circle" style="left:753px;top:1429px;width:278px;height:278px;background:var(--blue)">
    <svg width="150" height="120" viewBox="0 0 150 120"><g fill="#fff"><rect x="10" y="0" width="8" height="110"/><rect x="10" y="104" width="140" height="8"/><rect x="32" y="60" width="16" height="40"/><rect x="58" y="40" width="16" height="60"/><rect x="84" y="20" width="16" height="80"/><rect x="110" y="50" width="16" height="50"/></g></svg>
  </div>
</section>

<section class="feature">
  <div class="circle" style="left:110px;top:1768px;width:306px;height:306px;background:var(--purple)">
    <svg width="140" height="130" viewBox="0 0 140 130"><rect x="6" y="6" width="128" height="86" rx="6" fill="none" stroke="#fff" stroke-width="10"/><rect x="60" y="92" width="20" height="24" fill="#fff"/><rect x="40" y="114" width="60" height="10" rx="3" fill="#fff"/></svg>
  </div>
  <h3 style="left:525px;top:1822px;color:var(--purple)">Dashboards</h3>
  <p style="left:530px;top:1878px">Lorem Ipsum is simply dummy text of the printing and typesetting industry. Lorem Ipsum has been the industry's standard dummy text ever since the 1500s, when an unknown printer took a galley of type and scrambled it to make a type specimen book. It has survived not only five centuries, but also the leap into electronic typesetting, remaining essentially unchanged.</p>
</section>

<section class="feature">
  <h3 style="left:108px;top:2170px;color:var(--teal)">Data Integration</h3>
  <p style="left:110px;top:2226px">Lorem Ipsum is simply dummy text of the printing and typesetting industry. Lorem Ipsum has been the industry's standard dummy text ever since the 1500s, when an unknown printer took a galley of type and scrambled it to make a type specimen book. It has survived not only five centuries, but also the leap into electronic typesetting, remaining essentially unchanged.</p>
  <div class="circle" style="left:737px;top:2122px;width:306px;height:306px;background:var(--teal)">
    <svg width="110" height="130" viewBox="0 0 110 130"><g fill="#fff"><ellipse cx="55" cy="18" rx="52" ry="16"/><path d="M3 32c0 9 23 16 52 16s52-7 52-16v22c0 9-23 16-52 16S3 63 3 54z"/><path d="M3 68c0 9 23 16 52 16s52-7 52-16v22c0 9-23 16-52 16S3 99 3 90z"/><path d="M3 104c0 9 23 16 52 16s52-7 52-16v8c0 9-23 16-52 16S3 121 3 112z"/></g></svg>
  </div>
</section>

<div class="band"></div>
<h2 class="section-title resp-title">Our Responsive Websites</h2>
<div class="devices" role="img" aria-label="A desktop monitor, laptop, tablet and phone showing the same responsive website"></div>
<p class="resp-lead">Lorem Ipsum is simply dummy text of the printing and typesetting industry. Lorem Ipsum has been the industry's standard dummy text ever since the 1500s, when an unknown printer took a galley of type and scrambled it to make a type specimen book. It has survived not only five centuries, but also the leap into electronic typesetting, remaining essentially unchanged.</p>
<h2 class="section-title recent-title">Recent Responsive Layouts</h2>
<div class="rule"></div>

<article class="layout-card" style="left:110px">
  <div class="thumb" role="img" aria-label="Screenshot of a dark architecture website layout"></div>
  <h4>Responsive Layouts 1</h4>
  <p>Lorem Ipsum is simply dummy text of the printing and typesetting industry.</p>
  <span class="btn-details">View Details</span>
</article>
<article class="layout-card" style="left:445px">
  <div class="thumb" role="img" aria-label="Screenshot of a teal online shop layout" style="background:linear-gradient(180deg,#1fa89a 0 45%,#f2f2f2 45%)"></div>
  <h4>Responsive Layouts 2</h4>
  <p>Lorem Ipsum is simply dummy text of the printing and typesetting industry.</p>
  <span class="btn-details">View Details</span>
</article>
<article class="layout-card" style="left:780px">
  <div class="thumb" role="img" aria-label="Screenshot of a dark blue template website layout" style="background:linear-gradient(160deg,#0f2235,#3b6f8f)"></div>
  <h4>Responsive Layouts 3</h4>
  <p>Lorem Ipsum is simply dummy text of the printing and typesetting industry.</p>
  <span class="btn-details">View Details</span>
</article>

<footer>
  <div class="foot-brand"><div class="brand-name">Korvale</div><div class="brand-tag">Korvale Integration Solutions</div></div>
  <div class="foot-col" style="left:364px"><h5>Home Links</h5><ul><li>Home</li><li>About Us</li><li>Our Services</li><li>Events</li><li>Careers</li><li>Contact Us</li></ul></div>
  <div class="foot-col" style="left:528px"><h5>Other Links</h5><ul><li>Privacy Policy</li><li>Terms &amp; Conditions</li></ul></div>
  <div class="foot-col" style="left:694px;width:240px"><h5>Contact Us</h5>
    <div class="contact-row"><i></i><span>Lindenweg 24,<br>10115 Harbury</span></div>
    <div class="contact-row"><i></i><span>Telephone: +00 12 3456 7890</span></div>
    <div class="contact-row"><i></i><span>E-mail: hello@korvale-example.com</span></div>
  </div>
  <div class="foot-col" style="left:941px"><h5>Connect With Us</h5>
    <div class="follow"><span>Facelink</span><i></i></div>
    <div class="follow"><span>Chirper</span><i></i></div>
  </div>
  <div class="copy-rule"></div>
  <div class="copy">© 2014 Company Name . All Rights Reserved</div>
</footer>

</body>
</html>
```